Business Card Design Project

Combined with our Logo design project we are also after a template business card for our business "Veltrora"

We are a business to business firm that provides professional turnkey aerial (Drone) asset inspection solutions (Video/Photo/Survey/Thermal) for customers like Electrical, Water and Gas utilities, Energy generation companies and such.

The final design should be communicate safety (first and foremost), clean, reliabie and trust worthy

Target Market(s)

Business to business, particularly conservative large business owners whom are risk adverse.

Industry/Entity Type

Safety

Requirements
Must have
• Clean and fresh

```html
<!DOCTYPE html>
<html lang="en">
<head>
<meta charset="utf-8">
<title>Veltrora Business Card</title>
<link rel="stylesheet" href="https://fonts.googleapis.com/css2?family=Montserrat:wght@400;500;600&display=swap">
<style>
  :root {
    --backdrop: #2e2e30;
    --card: #f7f7f5;
    --ink: #2c2c2e;
    --ink-soft: #4a4a4d;
    --brand-blue: #24558f;
    --dot-blue: #2f63a0;
  }
  * { box-sizing: border-box; margin: 0; padding: 0; }
  html, body {
    width: 1200px;
    height: 1000px;
    overflow: hidden;
    background: var(--backdrop);
    font-family: "Montserrat", Arial, sans-serif;
  }
  .stage {
    width: 1200px;
    height: 1000px;
    display: flex;
    align-items: center;
    justify-content: center;
  }
  .business-card {
    position: relative;
    width: 860px;
    height: 500px;
    background: var(--card);
    color: var(--ink);
  }
  .brand {
    position: absolute;
    left: 190px;
    top: 62px;
    display: flex;
    align-items: center;
    gap: 16px;
  }
  .brand-mark {
    width: 46px;
    height: 46px;
    border-radius: 50%;
    background: var(--brand-blue);
  }
  .brand-name {
    font-weight: 600;
    font-size: 58px;
    letter-spacing: 1px;
    line-height: 1;
    color: var(--brand-blue);
    text-transform: uppercase;
  }
  .holder {
    position: absolute;
    right: 70px;
    top: 132px;
    text-align: right;
  }
  .holder-name {
    font-weight: 400;
    font-size: 31px;
    letter-spacing: 1px;
    line-height: 1.1;
  }
  .holder-role {
    font-size: 17px;
    letter-spacing: 1.5px;
    color: var(--ink-soft);
    margin-top: 4px;
  }
  .dot-rule {
    position: absolute;
    height: 6px;
    background: radial-gradient(circle, var(--dot-blue) 2.6px, transparent 3.1px) repeat-x left center / 11px 6px;
  }
  .dot-rule--title { left: 330px; right: 64px; top: 212px; }
  .dot-rule--middle { left: 60px; right: 64px; top: 336px; }
  .dot-rule--base { left: 60px; right: 64px; top: 470px; }
  .website {
    position: absolute;
    left: 62px;
    top: 300px;
    font-size: 17px;
    letter-spacing: 0.5px;
  }
  .contact {
    position: absolute;
    left: 420px;
    top: 242px;
    display: grid;
    grid-template-columns: 78px auto;
    row-gap: 9px;
    font-size: 17px;
    letter-spacing: 0.4px;
  }
  .contact dt {
    font-size: 15px;
    letter-spacing: 1px;
    color: var(--ink-soft);
    text-align: right;
    padding-right: 12px;
    line-height: 21px;
  }
  .contact dd { line-height: 21px; }
  .address {
    position: absolute;
    left: 62px;
    top: 366px;
    font-style: normal;
    font-size: 18px;
    line-height: 30px;
    letter-spacing: 0.4px;
  }
</style>
</head>
<body>
<main class="stage">
  <section class="business-card" aria-label="Veltrora business card">
    <div class="brand">
      <span class="brand-mark" aria-hidden="true"></span>
      <span class="brand-name">Veltrora</span>
    </div>

    <div class="holder">
      <p class="holder-name">DANIEL HART</p>
      <p class="holder-role">PRESIDENT</p>
    </div>

    <div class="dot-rule dot-rule--title" aria-hidden="true"></div>

    <p class="website">www.veltrora.com.au</p>

    <dl class="contact">
      <dt>MOBILE</dt><dd>+61 (03) 5550 1827</dd>
      <dt>PHONE</dt><dd>1800 555019</dd>
      <dt>EMAIL</dt><dd>danielhart@veltrora.com.au</dd>
    </dl>

    <div class="dot-rule dot-rule--middle" aria-hidden="true"></div>

    <address class="address">
      48 Harbour Rd<br>
      Eastbrook NSW 2190<br>
      Australia
    </address>

    <div class="dot-rule dot-rule--base" aria-hidden="true"></div>
  </section>
</main>
</body>
</html>
```